International Vacuum Business Needs Brochure Design

We need a flyer 8 1/2" x 11" booklet style (folded in half) flyer design for a new company based in Toronto called "Swivo-Lux". We will be selling and installing a proprietary central vacuum system that is one of a kind to the condominium market mainly through various large builders throughout the country as well as a second distribution chain at a retail level. Our product has a very unique retractable hose system that allows the hose to be stored away within the walls of a space all by the push of a button. "No more hoses laying around the house" The design should communicate the following terms " sleek, discreet, convenient, sophisticated, modern"
Updates
Reason: Hello All,
I have extended the deadline by a few days so i can spend some time reviewing all the designs and try to finalize a decision.
Thank you for all the designs!!
Target Market(s)
Our target market is male/female aged 25-65, more so focussing on 25-50.
Industry/Entity Type
Retail
Requirements
Must have
- The brochure must have an amazing, really catchy front cover, demonstrating our logo and the unit we sell. Back page should have all our contact information and once again a product picture. The Pelm Ovra symbol should be smaller than our logo and on the inner pages of the brochure, not on the front
Our address and contact information as below
Swivo-Lux Inc.
517 Harnett Ave.
Kelvale, ON
K7P2R9
Office 555.203.6614
Fax 555.718.2093
Toll 555.346.8120
www.swivolux.example
Nice to have
- I would like to see a picture of a clean modern space possibly in a condominium looking out to a great view. Want to send that message that this unit can make your life relaxed and easy. Must have for every condominium space.
New age of vacuuming!!
Innovation
Should not have
- A traditional feel to it.

```html
<!DOCTYPE html>
<html lang="en">
<head>
<meta charset="utf-8">
<title>Swivo-Lux Brochure</title>
<link rel="stylesheet" href="https://fonts.googleapis.com/css2?family=Open+Sans:wght@400;600&family=Yellowtail&display=swap">
<style>
  :root {
    --red: #c8101a;
    --red-deep: #7a0c12;
    --red-dark: #4a0709;
    --black: #050505;
    --white: #ffffff;
    --silver: #d7d7d7;
    --canvas: #e6e4e1;
    --photo-sky: #bcd6e6;
    --photo-floor: #9c948a;
    --photo-wall: #d8d4cc;
  }
  * { box-sizing: border-box; margin: 0; padding: 0; }
  html, body { width: 1200px; height: 900px; overflow: hidden; background: var(--canvas); }
  body { position: relative; font-family: "Open Sans", Arial, sans-serif; }

  .page { position: absolute; overflow: hidden; box-shadow: 0 6px 18px rgba(0,0,0,.25); }
  .page svg.shapes { position: absolute; inset: 0; width: 100%; height: 100%; }

  /* Shared brand line */
  .brand { position: absolute; display: flex; align-items: center; gap: 6px; font-family: "Open Sans", Arial, sans-serif; font-weight: 400; white-space: nowrap; }
  .brand-square { width: 14px; height: 14px; flex: none; }
  .tagline { position: absolute; font-size: 6px; letter-spacing: 2.4px; text-transform: uppercase; white-space: nowrap; }

  /* Back cover */
  .back-cover { left: 50px; top: 50px; width: 270px; height: 418px; background: var(--black); }
  .back-cover .brand { left: 62px; top: 140px; color: var(--red); font-size: 19px; }
  .back-cover .brand-square { background: var(--red); }
  .back-cover .tagline { left: 82px; top: 166px; color: var(--red); }
  .contact { position: absolute; left: 0; width: 100%; text-align: center; color: var(--white); font-size: 7.5px; line-height: 1.45; }
  .contact-title { top: 190px; font-style: italic; }
  .contact-lines { top: 222px; }
  .contact-address { top: 282px; }

  /* Front cover */
  .front-cover { left: 345px; top: 50px; width: 270px; height: 418px; background: var(--red); }
  .front-cover .brand { left: 20px; top: 26px; color: var(--white); font-size: 22px; }
  .front-cover .brand-square { background: var(--white); width: 16px; height: 16px; }
  .front-cover .tagline { left: 44px; top: 55px; color: var(--white); }
  .room-photo { position: absolute; inset: 0;
    clip-path: polygon(0 120px, 270px 250px, 270px 372px, 0 372px);
    background: linear-gradient(180deg, var(--photo-sky) 0%, #e9eef0 45%, var(--photo-wall) 62%, var(--photo-floor) 100%); }
  .unit-photo { position: absolute; left: 198px; top: 72px; width: 56px; height: 120px;
    background: linear-gradient(90deg, #f4f4f4, #d9d9dc); border: 2px solid var(--white); }

  /* Inner spread */
  .inner-spread { left: 625px; top: 420px; width: 540px; height: 418px; background: var(--black); }
  .section-title { position: absolute; font-family: "Yellowtail", "Brush Script MT", cursive; font-weight: 400; color: var(--red); font-size: 22px; line-height: 1; white-space: nowrap; }
  .copy { position: absolute; color: var(--white); font-size: 6.6px; line-height: 1.42; }
  .photo { position: absolute; border: 2px solid var(--red-deep); }
  .photo-install { left: 22px; top: 82px; width: 96px; height: 150px; background: linear-gradient(90deg, #cfc6b4 0%, #f2f0ec 40%, #e6e2da 70%, #a49a86 100%); }
  .photo-dock { left: 262px; top: 54px; width: 78px; height: 130px; background: linear-gradient(90deg, #e8e6e1 0%, #f7f7f5 50%, #b7ad98 100%); }
  .photo-bag { left: 160px; top: 282px; width: 106px; height: 70px; background: linear-gradient(135deg, #ebe7e0 0%, #c4bcae 55%, #3a3a3a 100%); }
  .photo-hose { left: 272px; top: 210px; width: 86px; height: 148px; background: linear-gradient(90deg, #6f93c8 0%, #e8ecf2 45%, #f6f6f6 70%, #cfcfcf 100%); }
  .product-mark { position: absolute; left: 416px; top: 138px; display: flex; align-items: center; gap: 5px; color: var(--red); font-size: 15px; font-weight: 400; white-space: nowrap; }
  .product-mark .square { width: 11px; height: 11px; background: var(--red); }
  .specs { display: block; margin-top: 10px; }
</style>
</head>
<body>

<section class="page back-cover">
  <svg class="shapes" viewBox="0 0 270 418" aria-hidden="true">
    <polygon points="60,0 270,0 270,86" fill="var(--red)"/>
    <polygon points="40,0 60,0 270,86 270,104" fill="var(--red-dark)"/>
    <line x1="40" y1="0" x2="270" y2="104" stroke="var(--silver)" stroke-width="2"/>
    <rect x="0" y="384" width="270" height="3" fill="var(--silver)"/>
    <rect x="0" y="388" width="270" height="30" fill="var(--red-deep)"/>
  </svg>
  <div class="brand"><span class="brand-square"></span>Swivo-Lux</div>
  <div class="tagline">Clean Without Clutter</div>
  <p class="contact contact-title">Contact us:</p>
  <p class="contact contact-lines">555 203 6614<br>info@swivolux.example<br>www.swivolux.example</p>
  <p class="contact contact-address">517 Harnett Ave.<br>Kelvale, ON K7P2R9<br>Canada</p>
</section>

<section class="page front-cover">
  <div class="room-photo" role="img" aria-label="Bright modern condominium living room with white sofas overlooking the sea"></div>
  <svg class="shapes" viewBox="0 0 270 418" aria-hidden="true">
    <polygon points="0,104 0,118 270,248 270,234" fill="var(--red-dark)"/>
    <line x1="0" y1="119" x2="270" y2="249" stroke="var(--white)" stroke-width="2.5"/>
    <rect x="0" y="372" width="270" height="3" fill="var(--white)"/>
    <rect x="0" y="376" width="270" height="42" fill="var(--red-deep)"/>
  </svg>
  <div class="brand"><span class="brand-square"></span>Swivo-Lux</div>
  <div class="tagline">Clean Without Clutter</div>
  <div class="unit-photo" role="img" aria-label="Tall white wall-mounted vacuum hose unit"></div>
</section>

<section class="page inner-spread">
  <svg class="shapes" viewBox="0 0 540 418" aria-hidden="true">
    <rect x="0" y="0" width="540" height="20" fill="var(--red-deep)"/>
    <rect x="0" y="22" width="540" height="3" fill="var(--silver)"/>
    <rect x="0" y="226" width="540" height="22" fill="var(--red-deep)"/>
    <rect x="360" y="178" width="180" height="14" fill="var(--red-dark)"/>
    <rect x="0" y="378" width="540" height="3" fill="var(--silver)"/>
    <rect x="0" y="382" width="540" height="36" fill="var(--red-deep)"/>
  </svg>

  <h2 class="section-title" style="left:70px; top:54px;">Simple</h2>
  <div class="photo photo-install" role="img" aria-label="White wall unit installed beside a hallway door"></div>
  <p class="copy" style="left:128px; top:82px; width:128px;">Installation of the Pelm Ovra is Simple. Pelm Ovra™ fits between two household wall studs on an interior wall space and can be generally be installed in less then an hour. Have your electrician hard wire or simply plug and play from any 110/120Volt outlet.</p>

  <h2 class="section-title" style="left:306px; top:30px;">On Demand</h2>
  <div class="photo photo-dock" role="img" aria-label="Open docking station with the hose pulled out"></div>
  <p class="copy" style="left:350px; top:54px; width:160px;">Total control is at your fingertips with Pelm Ovra™. Want more hose? Simply push the "out" button... All done? A quick push of the "in" button will retract up to 45 feet of hose back into the hose docking station.</p>
  <div class="product-mark"><span class="square"></span>Pelm Ovra</div>

  <div class="photo photo-hose" role="img" aria-label="Close-up of the hose handle with control buttons"></div>
  <p class="copy" style="left:372px; top:204px; width:152px;">Imagine a system with abundant vacuum performance. A system with the versatility of a central vacuum.<br>A system that automatically stores away the hose on demand with no effort.<br>A system that makes vacuuming easier. Such a system that would do it all... Pelm Ovra™ by Swivo-Lux<span class="specs">Suction 142"<br>Airwatts 500</span></p>

  <h2 class="section-title" style="left:116px; top:258px;">Convenience</h2>
  <p class="copy" style="left:20px; top:292px; width:134px;">Debris is stored inside an allergy resistant bag which captures 99.4% of pollens, bacteria and other harmful debris. Accessible compartment makes bag changes easy as well as service.</p>
  <div class="photo photo-bag" role="img" aria-label="Open low wall compartment holding the debris bag"></div>
</section>

</body>
</html>
```